Real Estate Listing Signs for standard Yard arms

I need real estate listing signs done, for the standard sized sign to be hung beneath a white yard arm. To match existing logo. Information to be included:
-Logo
-Business name
-Phone number
-Marden Fosk Tundra Circle & Marden Fosk realty logos (smaller print)

Colors to be Red and anywhere in the gray scale between black and white, or a combination of those.

Target Market(s)

Drive by visuals

Industry/Entity Type

Real Estate Agent

Colors

Designer to choose only greyscale colors for use in the design.

Requirements
Must have
• My Logo and business name in same/similar font to whats provided, the MF tundra circle logo (small on bottom or corner somewhere), My phone number, and a decent amount of red coloration on the sign.

```html
<!DOCTYPE html>
<html lang="en">
<head>
<meta charset="utf-8">
<title>Brenwick Homes – Yard Sign Presentation</title>
<link rel="stylesheet" href="https://fonts.googleapis.com/css2?family=Montserrat:wght@300;400;600;700;800&display=swap">
<style>
  :root {
    --red: #ff1b1f;
    --red-deep: #c80a0e;
    --red-dark: #a8070a;
    --white: #ffffff;
    --paper: #f4f4f4;
    --ink: #1e1e1e;
    --charcoal: #222222;
    --grey: #555555;
  }
  * { box-sizing: border-box; margin: 0; padding: 0; }
  html, body { width: 1200px; height: 3000px; overflow: hidden; }
  body {
    position: relative;
    background: var(--white);
    font-family: "Montserrat", Arial, sans-serif;
    color: var(--ink);
  }
  .block { position: absolute; }

  /* brand mark: plain square + name */
  .mark { display: flex; flex-direction: column; align-items: center; gap: 18px; }
  .mark-square { display: block; background: var(--red); }
  .mark-name {
    font-weight: 800; text-transform: uppercase; text-align: center;
    line-height: 0.95; letter-spacing: 1px;
  }
  .mark-row { flex-direction: row; }

  /* hero */
  .hero-panel { left: 0; top: 0; width: 600px; height: 600px; background: var(--red); }
  .hero-panel .mark { position: absolute; left: 0; right: 0; top: 150px; }
  .hero-panel .mark-square { width: 110px; height: 110px; background: var(--white); }
  .hero-panel .mark-name { color: var(--white); font-size: 62px; }

  .hero-mark { left: 760px; top: 45px; width: 300px; }
  .hero-mark .mark { gap: 14px; }
  .hero-mark .mark-square { width: 70px; height: 70px; }
  .hero-mark .mark-name { font-size: 22px; color: var(--ink); }

  /* signs */
  .sign {
    position: absolute; background: var(--white); overflow: hidden;
    box-shadow: 0 6px 18px rgba(0,0,0,0.18);
  }
  .sign-top { position: absolute; left: 0; top: 0; width: 100%; }
  .sign .mark { position: absolute; left: 0; right: 0; }
  .sign .mark-name { color: var(--ink); }
  .phone {
    position: absolute; left: 0; right: 0;
    display: flex; align-items: center; justify-content: center;
    font-weight: 800; letter-spacing: 1px;
  }
  .phone-band { background: var(--red); color: var(--white); }
  .phone-plain { color: var(--red); }
  .brokerage {
    position: absolute; left: 0; right: 0; bottom: 0;
    background: var(--red-deep); color: var(--white);
    display: flex; align-items: center; gap: 16px;
  }
  .brokerage-center { justify-content: center; }
  .brokerage-left { padding-left: 30px; }
  .brokerage-rule { height: 4px; width: 70px; background: var(--white); }
  .brokerage-name { display: flex; flex-direction: column; line-height: 1; }
  .brokerage-main { font-weight: 700; font-size: 20px; text-transform: uppercase; }
  .brokerage-sub { font-weight: 600; font-size: 9px; letter-spacing: 1px; text-transform: uppercase; margin-top: 3px; }

  .sign-hero { left: 730px; top: 290px; width: 410px; height: 466px; background: var(--paper); }
  .sign-hero .mark { top: 50px; gap: 16px; }
  .sign-hero .mark-square { width: 96px; height: 96px; }
  .sign-hero .mark-name { font-size: 40px; }
  .sign-hero .phone { top: 275px; height: 106px; font-size: 50px; }
  .sign-hero .brokerage { height: 86px; }

  .sign-side { left: 150px; top: 752px; width: 405px; height: 406px; }
  .sign-side .mark { top: 82px; gap: 26px; }
  .sign-side .mark-square { width: 86px; height: 86px; }
  .sign-side .mark-name { font-size: 31px; }
  .sign-side .phone { top: 252px; height: 66px; font-size: 42px; }
  .sign-side .brokerage { height: 86px; background: var(--red-dark); }

  .sign-wave-a { left: 150px; top: 1245px; width: 405px; height: 395px; }
  .sign-wave-b { left: 645px; top: 1245px; width: 400px; height: 395px; }
  .sign-wave-a .mark, .sign-wave-b .mark { top: 72px; gap: 26px; }
  .sign-wave-a .mark-square, .sign-wave-b .mark-square { width: 80px; height: 80px; }
  .sign-wave-a .mark-name, .sign-wave-b .mark-name { font-size: 28px; }
  .sign-wave-a .phone { top: 255px; height: 64px; font-size: 42px; }
  .sign-wave-b .phone { top: 260px; height: 70px; font-size: 42px; }
  .sign-wave-a .brokerage { height: 74px; }
  .sign-wave-b .brokerage { height: 64px; }

  /* brief */
  .brief-band { left: 0; top: 1760px; width: 1200px; height: 570px; }
  .brief-band svg { position: absolute; left: 0; top: 0; }
  .brief-mark { left: 66px; top: 1862px; }
  .brief-mark .mark { gap: 12px; }
  .brief-mark .mark-square { width: 64px; height: 64px; background: var(--white); }
  .brief-mark .mark-name { color: var(--white); font-size: 32px; }
  .brief-text {
    right: 74px; top: 1868px; width: 900px;
    color: var(--white); font-weight: 300; font-size: 25px; line-height: 1.32;
    text-align: right;
  }

  /* dark band */
  .dark-band { left: 0; top: 2330px; width: 1200px; height: 266px; background: var(--charcoal); }
  .dark-mark { left: 120px; top: 2200px; width: 640px; }
  .dark-mark .mark { gap: 26px; }
  .dark-mark .mark-square { width: 240px; height: 240px; background: var(--white); }
  .dark-mark .mark-name { color: var(--white); font-size: 60px; }
  .app-tile {
    left: 962px; top: 2380px; width: 160px; height: 160px;
    background: var(--red); border-radius: 22px;
    display: flex; align-items: center; justify-content: center;
  }
  .app-tile span { width: 76px; height: 76px; background: var(--white); }

  /* bottom photos */
  .photo { top: 2600px; height: 400px; }
  .photo-house { left: 0; width: 600px; background: linear-gradient(180deg, #ff2a2e 0%, #f0181c 55%, #b8161a 100%); }
  .photo-building { left: 600px; width: 600px; background: linear-gradient(90deg, #3a3a3a 0%, #2a2a2a 50%, #6a6a6a 100%); }
  .photo-house .mark { position: absolute; left: 0; right: 0; top: 72px; gap: 20px; }
  .photo-house .mark-square { width: 120px; height: 120px; background: var(--white); }
  .photo-house .mark-name { color: var(--white); font-size: 56px; }
  .photo-building .mark-square {
    position: absolute; left: 220px; top: 70px; width: 160px; height: 160px; background: var(--white);
  }
</style>
</head>
<body>

  <section class="block hero-panel">
    <div class="mark">
      <span class="mark-square"></span>
      <span class="mark-name">Brenwick<br>Homes</span>
    </div>
  </section>

  <div class="block hero-mark">
    <div class="mark">
      <span class="mark-square"></span>
      <span class="mark-name">Brenwick Homes</span>
    </div>
  </div>

  <article class="sign sign-hero">
    <div class="mark">
      <span class="mark-square"></span>
      <span class="mark-name">Brenwick<br>Homes</span>
    </div>
    <div class="phone phone-band">012-345-6789</div>
    <div class="brokerage brokerage-center">
      <span class="brokerage-rule"></span>
      <span class="brokerage-name">
        <span class="brokerage-main">MF Tundra Circle</span>
        <span class="brokerage-sub">Marden Fosk Realty</span>
      </span>
      <span class="brokerage-rule"></span>
    </div>
  </article>

  <article class="sign sign-side">
    <svg class="sign-top" width="405" height="120" viewBox="0 0 405 120" aria-hidden="true">
      <path d="M250 0 H405 V110 C380 40 330 14 250 0 Z" fill="var(--red)"/>
    </svg>
    <div class="mark">
      <span class="mark-square"></span>
      <span class="mark-name">Brenwick Homes</span>
    </div>
    <div class="phone phone-band">012-345-6789</div>
    <div class="brokerage brokerage-left">
      <span class="brokerage-name">
        <span class="brokerage-main">MF Tundra Circle</span>
        <span class="brokerage-sub">Marden Fosk Realty</span>
      </span>
    </div>
  </article>

  <article class="sign sign-wave-a">
    <svg class="sign-top" width="405" height="60" viewBox="0 0 405 60" aria-hidden="true">
      <path d="M0 0 H405 V40 C300 55 200 10 110 18 C60 22 25 32 0 40 Z" fill="var(--red)"/>
    </svg>
    <div class="mark">
      <span class="mark-square"></span>
      <span class="mark-name">Brenwick Homes</span>
    </div>
    <div class="phone phone-plain">012-345-6789</div>
    <div class="brokerage brokerage-left">
      <span class="brokerage-name">
        <span class="brokerage-main">MF Tundra Circle</span>
        <span class="brokerage-sub">Marden Fosk Realty</span>
      </span>
    </div>
  </article>

  <article class="sign sign-wave-b">
    <svg class="sign-top" width="400" height="60" viewBox="0 0 400 60" aria-hidden="true">
      <path d="M0 0 H400 V36 C330 20 270 12 200 24 C130 36 60 44 0 30 Z" fill="var(--red)"/>
    </svg>
    <div class="mark">
      <span class="mark-square"></span>
      <span class="mark-name">Brenwick Homes</span>
    </div>
    <div class="phone phone-band">012-345-6789</div>
    <div class="brokerage brokerage-center">
      <span class="brokerage-rule"></span>
      <span class="brokerage-name">
        <span class="brokerage-main">MF Tundra Circle</span>
        <span class="brokerage-sub">Marden Fosk Realty</span>
      </span>
      <span class="brokerage-rule"></span>
    </div>
  </article>

  <section class="block brief-band">
    <svg width="1200" height="570" viewBox="0 0 1200 570" aria-hidden="true">
      <path d="M0 40 H530 L600 0 L670 40 H1200 V570 H0 Z" fill="var(--red)"/>
    </svg>
  </section>

  <div class="block brief-mark">
    <div class="mark">
      <span class="mark-square"></span>
      <span class="mark-name">Brenwick<br>Homes</span>
    </div>
  </div>

  <p class="block brief-text">
    I need real estate listing signs done,<br>
    for the standard sized sign to be hung beneath a white yard arm.<br>
    To match existing logo. Information to be included:<br>
    -Logo<br>
    -Business name<br>
    -Phone number<br>
    -Marden Fosk Tundra Circle &amp; Marden Fosk realty logos (smaller print)<br>
    Colors to be Red and anywhere in the gray scale between black and white,<br>
    or a combination of those.
  </p>

  <section class="block dark-band"></section>

  <div class="block dark-mark">
    <div class="mark">
      <span class="mark-square"></span>
      <span class="mark-name">Brenwick Homes</span>
    </div>
  </div>

  <div class="block app-tile"><span></span></div>

  <section class="block photo photo-house" role="img" aria-label="Photo of a suburban family house with a red colour wash, brand name set over it">
    <div class="mark">
      <span class="mark-square"></span>
      <span class="mark-name">Brenwick<br>Homes</span>
    </div>
  </section>

  <section class="block photo photo-building" role="img" aria-label="Black and white photo of a modern glass office building with the brand square set over it">
    <span class="mark-square"></span>
  </section>

</body>
</html>
```